We need a card design for our company Harbor Lantern Partners. Our goal is to save people money on their disposal services. For this post card please put our logo in it. Please use these colors Pantone 576c and 418c or green and grey. We are giving you as the designer the opportunity to be creative with any other images. We are looking to have a fun eye catching postcard.
Please write:
Think you are stuck with your trash bill? Think again
We cut your neighbors disposal cost by 40%.

Please put down our information also,
Contact us
800.514.7262
melinda@plumcrest782.com
plumcrest782.com

```html
<!DOCTYPE html>
<html lang="en">
<head>
<meta charset="utf-8">
<title>Harbor Lantern Partners – Postcard</title>
<link rel="stylesheet" href="https://fonts.googleapis.com/css2?family=Roboto+Condensed:wght@700&family=Arimo:wght@400;700&display=swap">
<style>
  :root{
    --page:#e4e4e4;
    --teal:#015a6c;
    --teal-deep:#0b4656;
    --green:#6ea043;
    --grey:#4a4d4f;
    --white:#ffffff;
    --figure:#0c1a1e;
  }
  html,body{margin:0;padding:0;overflow:hidden;}
  body{width:1200px;height:1000px;background:var(--page);position:relative;}
  .postcard{
    position:absolute;left:40px;top:84px;width:895px;height:665px;
    transform:scale(1.2514);transform-origin:0 0;
    background:var(--teal);overflow:hidden;
    box-shadow:0 4px 14px rgba(0,0,0,.25);
  }
  .header{position:absolute;left:0;top:0;width:895px;height:100px;background:var(--white);border-bottom:5px solid var(--teal-deep);}
  .brand{position:absolute;left:250px;top:30px;display:flex;align-items:center;gap:10px;}
  .brand-mark{width:22px;height:22px;background:var(--green);}
  .brand-name{font-family:"Arimo",Arial,sans-serif;font-weight:700;font-size:21px;color:var(--grey);}
  .contact{position:absolute;left:632px;top:8px;margin:0;padding:0;list-style:none;}
  .contact li{display:flex;align-items:center;height:32px;font-family:"Arimo",Arial,sans-serif;color:var(--green);}
  .contact svg{width:28px;height:22px;margin-right:12px;flex:none;}
  .contact .web{font-weight:700;font-size:15px;}
  .contact .phone{font-size:17px;letter-spacing:.5px;}
  .contact .mail{font-size:14px;}
  .photo-strip{position:absolute;left:3px;top:110px;width:472px;height:233px;}
  .figure{
    position:absolute;left:465px;top:140px;width:140px;height:480px;
    background:linear-gradient(180deg,var(--figure) 0%,var(--figure) 90%,rgba(12,26,30,.3) 100%);
    border-radius:60px 60px 8px 8px;
  }
  .headline{
    position:absolute;left:558px;top:240px;margin:0;
    font-family:"Roboto Condensed","Arial Narrow",sans-serif;font-weight:700;
    font-size:46px;line-height:57px;color:var(--white);
  }
  .headline-answer{
    position:absolute;left:620px;top:452px;margin:0;
    font-family:"Roboto Condensed","Arial Narrow",sans-serif;font-weight:700;
    font-size:46px;line-height:57px;color:var(--white);
  }
  .offer{
    position:absolute;left:37px;top:543px;margin:0;
    font-family:"Arimo",Arial,sans-serif;font-size:32px;line-height:40px;color:var(--white);
  }
</style>
</head>
<body>
<main class="postcard">
  <header class="header">
    <div class="brand"><span class="brand-mark"></span><span class="brand-name">Harbor Lantern Partners</span></div>
    <ul class="contact">
      <li class="web">
        <svg viewBox="0 0 28 22"><g fill="none" stroke="#222" stroke-width="1.5"><circle cx="14" cy="11" r="9"/><ellipse cx="14" cy="11" rx="4" ry="9"/><line x1="5" y1="11" x2="23" y2="11"/><line x1="6.5" y1="6.5" x2="21.5" y2="6.5"/><line x1="6.5" y1="15.5" x2="21.5" y2="15.5"/></g></svg>
        www.plumcrest782.com
      </li>
      <li class="phone">
        <svg viewBox="0 0 28 22"><rect x="1" y="1" width="26" height="20" rx="3" fill="var(--green)"/><path d="M10 5c-1 1-1 3 1 6s4 5 6 6c1 0 2-1 2.5-2l-2.5-2-1.5 1c-1-.5-2.5-2-3-3l1-1.5L11.5 5z" fill="#fff"/></svg>
        800.514.7262
      </li>
      <li class="mail">
        <svg viewBox="0 0 28 22"><g fill="none" stroke="#222" stroke-width="1.5"><rect x="2" y="3" width="24" height="16"/><polyline points="2,3 14,13 26,3"/></g></svg>
        melinda@plumcrest782.com
      </li>
    </ul>
  </header>

  <svg class="photo-strip" viewBox="0 0 472 233">
    <rect x="0" y="0" width="290" height="233" fill="#ffffff"/>
    <g role="img" aria-label="Cupped hands holding soil with a young green seedling">
      <polygon points="0,0 290,0 237,233 0,233" fill="#efe6dc"/>
    </g>
    <polygon points="290,0 300,0 248,233 237,233" fill="var(--teal-deep)"/>
    <g role="img" aria-label="Scattered hundred-dollar bills">
      <polygon points="300,0 472,0 472,233 248,233" fill="#b9c2b4"/>
    </g>
  </svg>

  <div class="figure" role="img" aria-label="Silhouette of a thinking man with a thought bubble"></div>

  <h1 class="headline">Think you're<br>stuck with your<br>trash bill?</h1>
  <p class="headline-answer">..... Think<br>again</p>

  <p class="offer">We cut your neighbors<br>disposal cost by 40%.</p>
</main>
</body>
</html>
```